Trifold brochure

Please design a new trifold color brochure. I've uploaded our very outdated brochure for info purposes. I've uploaded some pictures of some items we've made as examples. Use stock photos or our photos, your preference. Use our new logo that is attached.

```html
<!DOCTYPE html>
<html lang="en">
<head>
<meta charset="utf-8">
<title>Harlow Steelworks – Trifold Brochure</title>
<link href="https://fonts.googleapis.com/css2?family=Montserrat:wght@400;500;600;700&display=swap" rel="stylesheet">
<style>
  :root{
    --bg:#ffffff;
    --brand:#2f3fa8;
    --accent:#4a73bf;
    --accent-dark:#3b62ad;
    --sky:#dbe6f3;
    --paper:#f3f4f6;
    --paper-2:#e9eaed;
    --ink:#333a44;
    --muted:#6b7380;
    --line:#4a73bf;
  }
  *{box-sizing:border-box;margin:0;padding:0}
  html,body{width:1200px;height:740px;overflow:hidden;background:var(--bg)}
  body{font-family:"Montserrat",Arial,sans-serif;color:var(--ink);position:relative}
  .sheet{position:absolute;top:150px;width:570px;height:440px;background:var(--paper);box-shadow:0 2px 10px rgba(0,0,0,.15);overflow:hidden}
  .sheet--outside{left:20px}
  .sheet--inside{left:610px;background:linear-gradient(180deg,#f2f4f8,#e1e9f3)}
  .panel{position:absolute;top:0;width:190px;height:440px}
  .p1{left:0}.p2{left:190px}.p3{left:380px}
  .fold{position:absolute;top:0;width:1px;height:440px;background:rgba(0,0,0,.06)}
  .abs{position:absolute}

  .brand{display:flex;align-items:center;gap:6px;font-weight:700;color:var(--brand);font-size:13px;letter-spacing:.5px;line-height:1}
  .brand__mark{width:12px;height:12px;background:var(--brand);flex:none}
  .tagline{font-size:6.5px;font-weight:600;color:var(--accent)}
  .values{font-size:8px;font-weight:700;color:var(--accent);word-spacing:6px}

  .cover-top{position:absolute;left:0;top:0;width:190px;height:130px;background:linear-gradient(180deg,#e9eff7,#c9d8ec)}
  .list-head{font-size:6.5px;font-weight:700;color:var(--accent);text-transform:uppercase;margin:0 0 5px}
  .list{list-style:none;font-size:7.5px;color:var(--ink);margin-bottom:10px}
  .list li{margin:0 0 6px 6px;position:relative;padding-left:10px}
  .list li::before{content:"";position:absolute;left:0;top:2px;width:4px;height:4px;background:var(--accent)}

  .photo{position:absolute}
  .band{position:absolute;background:var(--accent);color:#fff;text-align:center}
  .addr{font-size:6.5px}
  .phone{font-size:9px;font-weight:700}
  .web{font-size:6.5px}
  .mission-head{font-size:6.5px;font-weight:700;color:var(--accent);text-transform:uppercase;margin-bottom:4px}
  .mission{font-size:7px;line-height:1.45;text-align:justify}

  .products{position:absolute;left:12px;top:140px;width:166px}
  .products__head{background:var(--accent);color:#fff;padding:5px 7px}
  .products__title{font-size:9px;font-weight:700;letter-spacing:.5px}
  .products__intro{font-size:6px;line-height:1.3;margin-top:2px}
  .products table{width:100%;border-collapse:collapse;background:#fff;font-size:6.5px}
  .products td{border:1px solid var(--line);height:14px;padding:0 6px;width:50%}

  .contacts-head{display:flex;align-items:center;gap:6px;color:var(--accent);font-weight:700;font-size:9px;border-bottom:1px dotted var(--accent);padding-bottom:2px}
  .contacts-head span.dot{width:9px;height:9px;border-radius:50%;background:var(--accent)}
  .contact-text{font-size:6.8px;line-height:1.45;text-align:justify}
</style>
</head>
<body>

<!-- Outside spread -->
<section class="sheet sheet--outside">
  <div class="fold" style="left:190px"></div>
  <div class="fold" style="left:380px"></div>

  <!-- Back panel: services -->
  <div class="panel p1">
    <div class="cover-top"></div>
    <div class="abs" style="left:18px;top:42px">
      <div class="brand"><span class="brand__mark"></span>HARLOW STEELWORKS</div>
      <div class="tagline" style="margin:6px 0 0 18px">Custom Metal Fabrication</div>
    </div>
    <div class="abs" style="left:18px;top:148px;width:165px">
      <p class="list-head">Some of our services include...</p>
      <ul class="list">
        <li>Fabrication</li>
        <li>Mig, Tig Welding</li>
        <li>Fiber Optic Lasering</li>
        <li>Shearing</li>
        <li>Straightening, Forming, Bending</li>
        <li>Repairs</li>
        <li>Proto-typing</li>
        <li>Plasma cutting</li>
        <li>Painting, Powder Coating</li>
      </ul>
      <p class="list-head">We work with materials such as...</p>
      <ul class="list">
        <li>Stainless Steel</li>
        <li>Aluminum</li>
        <li>Carbon Steel</li>
        <li>Bronze</li>
        <li>Copper</li>
        <li>Lexan / Nomex</li>
      </ul>
    </div>
  </div>

  <!-- Middle panel -->
  <div class="panel p2" style="background:linear-gradient(90deg,#e6e7ea,#f4f4f6)">
    <div class="values abs" style="left:30px;top:70px">Quality Dependability Integrity</div>
    <div class="photo" role="img" aria-label="Photo of a large stainless steel industrial dryer unit outside a workshop" style="left:0;top:95px;width:190px;height:135px;background:linear-gradient(160deg,#c7c4bc,#8d8b86 55%,#5f5d58)"></div>
    <div class="band" style="left:0;top:230px;width:190px;height:110px;padding-top:38px">
      <p class="addr">4120 Mill Creek Rd. Ashford, VA 23000</p>
      <p class="phone">Phone (555)-014-2290</p>
      <p class="web" style="margin-top:4px">www.harlowsteelworks.com</p>
    </div>
    <div class="abs" style="left:32px;top:385px">
      <div class="brand"><span class="brand__mark"></span>HARLOW STEELWORKS</div>
    </div>
  </div>

  <!-- Front cover -->
  <div class="panel p3" style="background:linear-gradient(90deg,#eeeff1,#f7f7f8)">
    <div class="abs" style="left:26px;top:24px">
      <div class="brand"><span class="brand__mark"></span>HARLOW STEELWORKS</div>
      <div class="tagline" style="margin:6px 0 0 30px">Custom Metal Fabrication</div>
    </div>
    <div class="values abs" style="left:40px;top:70px">Quality Dependability Integrity</div>
    <div class="photo" role="img" aria-label="Photo of a welder at work with sparks, in blue tones" style="left:0;top:95px;width:190px;height:135px;background:linear-gradient(150deg,#2c3f7a,#4b5fb0 50%,#8fa0d8)"></div>
    <div class="band" style="left:160px;top:230px;width:30px;height:70px"></div>
    <div class="abs" style="left:18px;top:245px;width:140px">
      <p class="mission-head">Our Mission</p>
      <p class="mission">We supply our customers fabricated metal products that are designed &amp; produced with the highest quality, most competitive pricing, and the fastest lead-time in the industry!</p>
    </div>
    <div class="abs" style="left:30px;top:350px">
      <p class="addr">4120 Mill Creek Rd. Ashford, VA 23000</p>
      <p class="phone" style="color:var(--accent)">Phone (555)-014-2290</p>
      <p class="web" style="margin-top:4px">www.harlowsteelworks.com</p>
    </div>
  </div>
</section>

<!-- Inside spread -->
<section class="sheet sheet--inside">
  <div class="fold" style="left:190px"></div>
  <div class="fold" style="left:380px"></div>

  <div class="photo" role="img" aria-label="Photo of a stainless hopper on a white stand in the shop" style="left:0;top:0;width:190px;height:130px;background:linear-gradient(160deg,#a59a88,#7b7366 60%,#5c564d)"></div>
  <div class="photo" role="img" aria-label="Photo of the fabrication shop interior" style="left:190px;top:0;width:190px;height:110px;background:linear-gradient(160deg,#5a4e44,#3f3732)"></div>
  <div class="photo" role="img" aria-label="Photo of a long fabrication table inside the plant" style="left:380px;top:0;width:190px;height:120px;background:linear-gradient(160deg,#b9ac93,#8f8675 60%,#6f695d)"></div>

  <div class="products">
    <div class="products__head">
      <p class="products__title">PRODUCTS</p>
      <p class="products__intro">Our products are as diverse as our customer base. Some of the products we specialize in are listed</p>
    </div>
    <table>
      <tr><td>Enclosures</td><td>Conveyors</td></tr>
      <tr><td>Bins</td><td>Racks</td></tr>
      <tr><td>Tanks</td><td>Heated Parts</td></tr>
      <tr><td>Guards</td><td>Welding</td></tr>
      <tr><td>Jigs, Fixtures</td><td>Forming</td></tr>
      <tr><td>Baskets</td><td>Frames</td></tr>
      <tr><td>Pans</td><td>Modifications</td></tr>
      <tr><td>Duct Work</td><td>Channel</td></tr>
      <tr><td>Brackets</td><td>Panels</td></tr>
      <tr><td>Fittings</td><td>Cones</td></tr>
      <tr><td>Cladding</td><td>Discs</td></tr>
      <tr><td>Oxidizers</td><td>Shims</td></tr>
      <tr><td>Mixers</td><td>Covers</td></tr>
      <tr><td>Hoppers</td><td>Angles</td></tr>
      <tr><td>Ramps</td><td>Rails</td></tr>
      <tr><td>Carts</td><td>Clips</td></tr>
      <tr><td>Dryers</td><td>Transitions</td></tr>
    </table>
  </div>

  <div class="panel p2">
    <div class="photo" role="img" aria-label="Photo of a fabricated steel dust collector vessel with gauges" style="left:45px;top:110px;width:100px;height:175px;background:linear-gradient(180deg,#d8d8d8,#8a8a8a 60%,#4d4d4d)"></div>
    <div class="abs" style="left:45px;top:302px;width:110px">
      <div class="contacts-head"><span class="dot"></span>CONTACTS</div>
    </div>
    <p class="contact-text abs" style="left:18px;top:322px;width:156px">Our project managers have spent many years in the metal fabrication business. They are very knowledgeable and have vast experience in designing and producing items for different types of industries. Give them a call today and see how they can help you!</p>
    <div class="abs" style="left:14px;top:392px;width:170px;text-align:center">
      <p class="addr">4120 Mill Creek Rd. Ashford, VA 23000</p>
      <p class="phone" style="font-size:10px">Phone: (555)-014-2290</p>
      <p class="web">sales@harlowsteelworks.com | www.harlowsteelworks.com</p>
    </div>
  </div>

  <div class="panel p3">
    <div class="photo" role="img" aria-label="Photo of a steel tray rack on casters" style="left:35px;top:130px;width:125px;height:160px;background:linear-gradient(180deg,#b8ad78,#8c8455 60%,#4a452e)"></div>
    <div class="photo" role="img" aria-label="Photo of a conveyor line in a factory" style="left:25px;top:300px;width:150px;height:115px;background:linear-gradient(150deg,#d8ccb0,#8b8167 50%,#3f3b30)"></div>
  </div>
</section>

</body>
</html>
```